Flyer-Design für Apotheke
Zielgruppe
Wir sind eine Apotheke, mit Schwerpunkt Mutter-Kind / Wiegenhafen Apotheke (www.wiegenhafen Apotheke)
Zielgruppe: Wir haben uns zertifiziert und spezialisiert im Bereich Mütter / Kinderwunsch / Stillen / Babys etc. (Siehe Anbei unser aktueller Entwurf Mutter-Kind-Broschüre)
Wir haben zahlreiche Handouts zu spezifischen Themen von der LHTV und unserem Verein Wiegenhafen Apotheken für unser Kunden schon fertig gestellt (siehe ein Beispiel im Anhang, auf dem wir noch unser Logo eingefügt haben).
Die Handouts sind meist 4-seitig A5, im Anhang mit unserem Logo noch versehen.
Zu zwei Themen möchten wir jetzt noch selbst ein Handout erstellen.
1) Fieberthermometer
2) Schnuller
Ziel: 4-6 Seiten, wir wollen es dann bei Druckfuchs drucken lassen.
Zielgruppe: Mütter, die zu uns in die Apotheke kommen und beraten werden (konkret in diesen Beispielen zum Thema Fieberthermometer bzw. Schnuller. Damit sie was mit nach Hause nehmen können, möchten wir die Handouts erstellen.
Texte anbei, Graphische Umsetzung ggf. mit netten Baby/Mütterbildern o.ä. erwünscht
Aufgabenstellung
Einbau Logo Tolvena-Apotheke (siehe Anhang) ähnlich wie auf dem Flyer Ernährung
(als Logo ohne Adresse etc. und irgendwo unter mit Adresse, Telefon etc.)
Logo Wiegenhafen Apotheke DARF NICHT MIT DRAUF

```html
<!DOCTYPE html>
<html lang="de">
<head>
<meta charset="utf-8">
<title>Gewusst, wie! – Fieberthermometer und -messung</title>
<link href="https://fonts.googleapis.com/css2?family=Arimo:wght@400;700&display=swap" rel="stylesheet">
<style>
:root{
  --page:#ffffff;
  --panel:#eef1f7;
  --ink:#1b1b1b;
  --brand-red:#e30613;
  --logo-ink:#2a2a2a;
  --photo-warm:#e7cdb6;
  --photo-bed:#d9dbe4;
  --photo-cool:#c9ccd8;
  --social:#5a6b86;
}
*{margin:0;padding:0;box-sizing:border-box}
html,body{width:874px;height:1200px;overflow:hidden;background:var(--page)}
body{position:relative;font-family:"Arimo",Arial,sans-serif;color:var(--ink)}
.frame{position:absolute;inset:0;border:1px solid #bdbdbd}
.spread{position:absolute;left:54px;width:766px;height:535px;background:var(--panel)}
.spread--outer{top:35px}
.spread--inner{top:616px}

.logo{position:absolute;display:flex;align-items:flex-start;gap:3px;z-index:2}
.logo__name{font-weight:700;color:var(--logo-ink);letter-spacing:-.3px;line-height:.86}
.logo__dot{border-radius:50%;background:var(--brand-red);flex:none}
.logo--sm .logo__name{font-size:16px}
.logo--sm .logo__dot{width:8px;height:8px}
.logo--lg .logo__name{font-size:27px}
.logo--lg .logo__dot{width:13px;height:13px}

.section-title{position:absolute;font-size:11.2px;font-weight:400;white-space:nowrap}
.running-head{position:absolute;font-size:10.8px;white-space:nowrap}
.cover-title{position:absolute;font-weight:700;font-size:14.6px;white-space:nowrap;z-index:2}
.cover-sub{position:absolute;font-weight:700;font-size:11.4px;z-index:2}

.rule{position:absolute;height:3px;background:var(--brand-red)}
.photo{position:absolute}
.photo--warm{background:linear-gradient(135deg,#f1e4d6,var(--photo-warm))}
.photo--bed{background:linear-gradient(160deg,#f4eef0,var(--photo-bed))}
.photo--cool{background:linear-gradient(135deg,#e6e4ea,var(--photo-cool))}
.photo--device{background:linear-gradient(180deg,#f1f2f5,#ecdfe2);z-index:1}
.photo--oval{border-radius:50%;background:radial-gradient(ellipse at center,#d9c6c0,#b9bfd3);z-index:2}
.photo--glass{background:linear-gradient(90deg,#f3e9e4,#ead2c4 60%,#d8b3a0)}

.copy{position:absolute;font-size:7.3px;line-height:8px;white-space:nowrap}
.mark{display:inline-block;width:5px;height:5px;border:.5px solid #999;margin-right:1px;vertical-align:0}

.signoff{position:absolute;font-size:7.3px;line-height:8px}
.disclaimer{position:absolute;font-size:5.1px;line-height:7.3px;white-space:nowrap}
.folio{position:absolute;font-size:4.8px}

.contact{position:absolute;font-size:5.2px;line-height:6.4px;font-weight:700;letter-spacing:-.1px}
.contact__web{font-size:9.4px;line-height:11px;color:var(--brand-red);letter-spacing:-.3px}
.social{position:absolute;display:flex;gap:7px}
.social span{width:14px;height:14px;border-radius:2px;background:var(--social)}
</style>
</head>
<body>
<div class="frame"></div>

<section class="spread spread--outer">
  <div class="logo logo--sm" style="left:293px;top:34px"><span class="logo__name">Tolvena<br>Apotheke</span><span class="logo__dot"></span></div>

  <h2 class="section-title" style="left:26px;top:80px">Überblick unterschiedliche Messmethoden:</h2>

  <div class="rule" style="left:264px;top:90px;width:115px"></div>
  <div class="photo photo--warm" role="img" aria-label="Foto: Kind mit Hand an der Stirn und Teddybär" style="left:264px;top:97px;width:115px;height:74px"></div>
  <div class="rule" style="left:264px;top:264px;width:115px"></div>
  <div class="photo photo--bed" role="img" aria-label="Foto: Kind im Bett, Hand eines Erwachsenen prüft die Stirn" style="left:264px;top:268px;width:115px;height:75px"></div>

  <div class="copy" style="left:27px;top:122px">
    <p>5.Messung an der Stirn<br>Vorteil:<br><span class="mark"></span>Kontaktlos<br><span class="mark"></span>Messung im Schlaf möglich<br><span class="mark"></span>hygienisch, da Krankheitserreger nicht mit dem Thermometer<br>in Kontakt kommen<br><span class="mark"></span>schnelle Messergebnisse<br>Nachteil:<br><span class="mark"></span>Abweichung von der Körperkerntemperatur um -0,5°C<br><span class="mark"></span>Geeignet ab ca. 2 Jahren (je nach Modell)<br><span class="mark"></span>Stark abhängig von äußeren Einflüssen (Raum- und<br>Hauttemperatur, Verletzungen auf der Haut, etc.)<br><span class="mark"></span>Teurer als einfache Thermometer<br><span class="mark"></span>Handhabung erfordert gewisse Übung</p>
    <p style="margin-top:8px">Hinweise zur Anwendung:<br><span class="mark"></span>Bei vorherigen, äußeren Einflüssen (Mütze, auf Ohr gelegen,<br>&nbsp;warm gebadet, etc.) ca. 30 Minuten bis zur Messung abwarten<br><span class="mark"></span>Thermometer muss ebenfalls ca. 30 Minuten in stabiler<br>Umgebungstemperatur gelagert werden<br><span class="mark"></span>Haut auf Stirn bzw. Schläfe (je nach Modell) muss trocken<br>und sauber sein, da Feuchtigkeit durch Verdunstungskälte<br>die Messwerte beeinflussen kann</p>
    <p style="margin-top:6px">Fazit:<br>Die genauste Methode der Fiebermessung ist die rektale<br>Messung. Besonders bei Neugeborenen und Kindern mit<br>Fieberkrämpfen ist diese zu bevorzugen. Sollte sie nicht<br>durchführbar sein, ist die Messung am Ohr besonders für<br>Kinder eine geeignete Alternative. Hier ist jedoch ebenfalls<br>wie beim Stirnthermometer der geübte Umgang und der<br>Temperaturunterschied zur Körperkerntemperatur zu beachten.<br>&nbsp;Daher empfiehlt es sich nach Kauf des Messinstrumentes<br>die individuelle, gesunde Körpertemperatur zu bestimmen.<br>Die Messung unter den Achseln ist wegen hoher<br>Temperaturabweichungen generell nicht zu empfehlen.</p>
  </div>

  <p class="signoff" style="left:27px;top:428px">Bei weiteren Fragen helfen wir Ihnen gerne weiter.</p>
  <p class="signoff" style="left:27px;top:444px">Ihr babyfreundliches Team der Tolvena Apotheke Kellerau</p>

  <p class="disclaimer" style="left:27px;top:489px">Die vorliegenden Informationen wurden mit größtmöglicher Sorgfalt nach dem derzeitigen aktuellen Stand der Wissenschaft<br>zusammengestellt, dennoch übernehmen Verfasser und Herausgeber keine Gewähr. Es besteht kein Anspruch auf Vollständigkeit.</p>
  <span class="folio" style="left:348px;top:499px">Seite 4</span>

  <h1 class="cover-title" style="left:414px;top:106px">Gewusst, wie! – Fieberthermometer und -messung</h1>
  <p class="cover-sub" style="left:414px;top:131px">Informationsbroschüre</p>

  <div class="photo photo--device" role="img" aria-label="Foto: digitales Fieberthermometer mit flexibler roter Spitze" style="left:440px;top:150px;width:250px;height:300px"></div>

  <div class="logo logo--lg" style="left:446px;top:164px"><span class="logo__name">Tolvena<br>Apotheke</span><span class="logo__dot"></span></div>

  <div class="photo photo--oval" role="img" aria-label="Foto: Mädchen im Bett mit Teddybär und Thermometer" style="left:593px;top:348px;width:146px;height:104px"></div>

  <div class="contact" style="left:413px;top:456px">
    Lindenhofweg 8&nbsp;&nbsp;&nbsp; 90412 Kellerau<br>tel: 04711 / 550210&nbsp;&nbsp;&nbsp;fax: 550210-9<br>kontakt@tolvena-apotheke.de<br><span class="contact__web">www.tolvena-apotheke.de</span>
  </div>
  <div class="social" aria-label="Soziale Netzwerke" style="left:639px;top:470px"><span></span><span></span><span></span><span></span><span></span></div>

  <p class="disclaimer" style="left:411px;top:489px">Die vorliegenden Informationen wurden mit größtmöglicher Sorgfalt nach dem derzeitigen aktuellen Stand der Wissenschaft<br>zusammengestellt, dennoch übernehmen Verfasser und Herausgeber keine Gewähr. Es besteht kein Anspruch auf Vollständigkeit.</p>
</section>

<section class="spread spread--inner">
  <div class="logo logo--sm" style="left:34px;top:27px"><span class="logo__name">Tolvena<br>Apotheke</span><span class="logo__dot"></span></div>
  <p class="running-head" style="left:29px;top:76px">Gewusst, wie! – Fieberthermometer und -messung</p>
  <div class="rule" style="left:268px;top:91px;width:114px"></div>
  <div class="photo photo--cool" role="img" aria-label="Foto: Junge im Bett mit Thermometer im Mund und Teddybär" style="left:268px;top:95px;width:114px;height:76px"></div>
  <h2 class="section-title" style="left:31px;top:119px">Überblick unterschiedliche Messmethoden:</h2>
  <div class="rule" style="left:267px;top:252px;width:115px"></div>
  <div class="photo photo--bed" role="img" aria-label="Foto: krankes Kind im Bett mit Teddybär und Medikamenten" style="left:267px;top:257px;width:115px;height:75px"></div>

  <div class="copy" style="left:30px;top:146px">
    <p>1.Rektale Messung<br>Hierbei wird das Thermometer je nach Produkt 1-3 cm in den After<br>eingeführt und die Temperatur der Schleimhaut gemessen. Je nach<br>Modell erfolgt die Messung innerhalb von wenigen Sekunden<br>&nbsp;durch ein akustisches Signal, verfügt über Messwertspeicher,<br>Fieberalarm und beleuchtetem Anzeigefenster.<br>Vorteil:<br><span class="mark"></span>Genauste und zuverlässigste Messung, kommt der<br>Körperkerntemperatur am nächsten<br><span class="mark"></span>Für jedes Alter geeignet<br><span class="mark"></span>Leichte Reinigung, wasserdicht<br>Nachteil:<br><span class="mark"></span>Unangenehm, von Kindern &amp; Erwachsenen häufig nicht akzeptiert<br>Hinweise zur Anwendung:<br><span class="mark"></span>Zum leichteren Einführen: Thermometer mit flexibler Spitze<br>verwenden, alternativ mit etwas<br>&nbsp;Vaseline einfetten oder mit Wasser anfeuchten<br><span class="mark"></span>Bewährte Messpositionen:<br>-Babys: auf dem Rücken liegend mit hochgehaltenen Beinchen<br>-Kleinkinder: mit dem Bauch nach unten über den Schoß<br>-Ältere Kinder/Erwachsene: Seitenlage mit angezogenen Beinen</p>
    <p style="margin-top:3px">2.Sublinguale Messung<br>Hierbei wird die Temperatur unter der Zunge gemessen.<br>Vorteil:<br><span class="mark"></span>Hohe Akzeptanz<br>Nachteil:<br><span class="mark"></span>Abweichung von der Körperkerntemperatur von -0,3- 0,5°C<br><span class="mark"></span>Geeignet ab ca. 4-5 Jahren<br><span class="mark"></span>Verfälschungen möglich (geöffneten Mund, Speisen, Getränke, etc.)<br>Hinweise zur Anwendung:<br><span class="mark"></span>Richtige Platzierung der Spitze unter der Zunge, links oder rechts<br>des Zungenbändchens in der dortigen, sogenannten Wärmetasche<br><span class="mark"></span>Mund während der Messung schließen und durch die Nase atmen<br><span class="mark"></span>Um Verfälschungen zu vermeiden, sollten kalte oder heiße Speisen<br>&nbsp;und Getränke, Rauchen und Kaugummi kauen 10 Minuten vorher<br>unterlassen werden<br><span class="mark"></span>Während der Messung darf das Thermometer nicht bewegt werden<br>und der Kontakt zur Schleimhaut muss gegeben sein</p>
  </div>

  <p class="disclaimer" style="left:30px;top:459px">Die vorliegenden Informationen wurden mit größtmöglicher Sorgfalt nach dem<br>derzeitigen aktuellen Stand der Wissenschaft zusammengestellt, dennoch übernehmen<br>Verfasser und Herausgeber keine Gewähr. Es besteht kein Anspruch auf Vollständigkeit.</p>
  <span class="folio" style="left:29px;top:497px">Seite 2</span>

  <div class="logo logo--sm" style="left:668px;top:24px"><span class="logo__name">Tolvena<br>Apotheke</span><span class="logo__dot"></span></div>
  <p class="running-head" style="left:418px;top:74px">Gewusst, wie! – Fieberthermometer und -messung</p>
  <div class="rule" style="left:657px;top:89px;width:85px"></div>
  <div class="photo photo--glass" role="img" aria-label="Foto: Hand hält ein Glas-Fieberthermometer mit Skala" style="left:657px;top:93px;width:85px;height:341px"></div>
  <h2 class="section-title" style="left:418px;top:116px">Überblick unterschiedliche Messmethoden:</h2>

  <div class="copy" style="left:419px;top:144px">
    <p>3.Schnullerthermometer<br>Dieses Thermometer wird wie ein Schnuller in den Mund des Kindes<br>&nbsp;gesteckt und misst nach ca. 5 Minuten die Temperatur.<br>Vorteil:<br><span class="mark"></span>Evtl. höhere Akzeptanz beim Kind, da es den Schnuller schon kennt<br>Nachteil:<br><span class="mark"></span>Für Kinder bis zu einem Alter von ca. 3 Jahren<br><span class="mark"></span>Lange Messdauer<br><span class="mark"></span>Verfälschungen möglich (geöffneten Mund v.a. bei verschnupften<br>&amp; weinenden Kindern, Speisen, Getränke)</p>
    <p style="margin-top:8px">Hinweise zur Anwendung:<br><span class="mark"></span>Mund während der Messung schließen und durch die Nase atmen<br><span class="mark"></span>Um Verfälschungen zu vermeiden, sollten kalte oder heiße Speisen<br>&nbsp;und Getränke 10 Minuten vorher unterlassen werden</p>
    <p style="margin-top:4px">4.Messung im Ohr<br>Hierbei nimmt ein Infrarotsensor im Thermometerkopf die vom<br>Trommelfell ausgehende Wärmestrahlung auf.<br>Vorteil:<br><span class="mark"></span>Schnell und präzise<br><span class="mark"></span>Für jedes Alter geeignet<br><span class="mark"></span>Messung im Schlaf möglich<br><span class="mark"></span>hygienisch, da Krankheitserreger nicht mit dem Thermometer in<br>Kontakt kommen<br>Nachteil:<br><span class="mark"></span>Abweichung von der Körperkerntemperatur um -0,5°C<br><span class="mark"></span>Verfälschung möglich (Ohrschmalz, sehr enge Gehörgänge)<br><span class="mark"></span>Teurer als einfache Thermometer<br><span class="mark"></span>Handhabung erfordert gewisse Übung</p>
    <p style="margin-top:8px">Hinweise zur Anwendung:<br><span class="mark"></span>Bei vorherigen, äußeren Einflüssen (Mütze, auf Ohr gelegen,<br>warm gebadet, etc.) ca. 30 Minuten bis zur Messung abwarten<br><span class="mark"></span>Nicht im Ohr messen, wenn davor Ohrentropfen verwendet wurden<br>&nbsp;oder sich Blut bzw. Sekret im Gehörgang befindet<br><span class="mark"></span>Bei Entzündungen am äußeren Ohr keine Messung mit dem<br>Ohrthermometer vornehmen<br><span class="mark"></span>Handhabung: Damit die Wärmestrahlung den Sensor ungehindert<br>erreicht, muss der natürlich gekrümmte Gehörgang zuvor „begradigt“ werden<br>-Kinder bis 1 Jahr: Ohr gerade nach hinten ziehen<br>-Kinder ab 1 Jahr: Ohr nach oben und hinten ziehen</p>
  </div>

  <span class="folio" style="left:726px;top:497px">Seite&nbsp; 3</span>
</section>
</body>
</html>
```